SIGN UP PAGE AND CHECK OUT PROCESS DESIGN NEEDED

I offer a subscription service. Two products that offer the same exact features just two different prices as the cheaper product offers limited of all the features....<br/><br/>PLEASE USE EXISTING THEME OF CURRENT DESIGN JUST MAKE AN IMPROVED SIGN UP PAGE. <br/><br/><br/>NEED SIGN UP PAGE for a subscription service..... <br/>This is my current sign up page, only offers one product: https://www.brightloomrewards.biz/?page=signup <br/><br/>Please use all the same fields and content listed on this sign up page also please do a fake sign up to see the credit card page. I also need the credit card page to be designed....or if you want to combine the sign up and credit card page, etc. all in one I am open for that too....my goal is a super quick an easy sign up for customer. <br/><br/> AL A CARTE PROGRAM<br/>1 CERTIFICATE TYPE EACH MONTH<br/>$49/MTH MONTH TO MONTH BASIS NO CONTRACTS<br/>$239 ONE TIME PAYMENT FOR 6 MTHS OF SERVICE<br/>$399 ONE TIME PAYMENT FOR 12 MONTHS OF SERVICE<br/><br/>FEATURES:<br/><br/>UNLIMITED CERTIFICATE PDF DOWNLOADS<br/><br/>UNLIMITED E-MAIL CERTIFICATES<br/><br/>UNLIMITED TEXT/SMS CERTIFICATES<br/><br/>UNLIMITED API USAGE<br/><br/>UNLIMITED WEB BANNER CERTIFICATES<br/><br/>FULL REDEMPTION TRACKING<br/><br/>CERTIFICATE DISTRIBUTION REPORTS<br/><br/>WHITE LABEL REDEMPTION SITE<br/><br/>END USER MARKETING VIDEOS<br/><br/>MARKETING POSTERS AND FLYERS<br/><br/>PRODUCT DESCRIPTIONI BROCHURES<br/><br/>THE LATEST TIPS<br/><br/>SEPERATE REDEMPTION WEBSITES<br/><br/>CONTACT US 24/7<br/><br/>AFFILIATE PROGRAM<br/><br/>DISCOUNT TRAVEL BOOKING ENGINE<br/><br/>UNLIMITED PROGRAM<br/>UNLIMITED AMOUNTS OF ALL THE CERTIFICATES<br/>$99/MTH MONTH TO MONTH BASIS NO CONTRACTS<br/>$495 ONE TIME PAYMENT FOR 6 MTHS OF SERVICE<br/>$2,295 ONE TIME PAYMENT FOR 12 MONTHS OF SERVICE<br/><br/>FEATURES:<br/><br/>UNLIMITED CERTIFICATE PDF DOWNLOADS<br/><br/>UNLIMITED E-MAIL CERTIFICATES<br/><br/>UNLIMITED TEXT/SMS CERTIFICATES<br/><br/>UNLIMITED API USAGE<br/><br/>UNLIMITED WEB BANNER CERTIFICATES<br/><br/>FULL REDEMPTION TRACKING<br/><br/>CERTIFICATE DISTRIBUTION REPORTS<br/><br/>WHITE LABEL REDEMPTION SITE<br/><br/>END USER MARKETING VIDEOS<br/><br/>MARKETING POSTERS AND FLYERS<br/><br/>PRODUCT DESCRIPTIONI BROCHURES<br/><br/>THE LATEST TIPS<br/><br/>SEPERATE REDEMPTION WEBSITES<br/><br/>CONTACT US 24/7<br/><br/>AFFILIATE PROGRAM<br/><br/>DISCOUNT TRAVEL BOOKING ENGINE<br/><br/><br/>

Target Market(s)

B2B SMALL BUSINESS OWNERS
MARKETERS
ADVERTISERS

Industry/Entity Type

Digital Marketing

Number of Pages Required

3 page

Colors

Designer to choose colors to be used in the design.

Requirements
Must have
• MUST MATCH EXISTING THEME
Nice to have
• A VERY MODERN DESIGN

```html
<!DOCTYPE html>
<html lang="en">
<head>
<meta charset="utf-8">
<title>Brightloom Rewards – Sign Up and Payment Pages</title>
<link href="https://fonts.googleapis.com/css2?family=Open+Sans:wght@400;600;700&display=swap" rel="stylesheet">
<style>
:root{
  --navy:#141a2e;
  --blue:#1f5fd6;
  --blue-dark:#174bb0;
  --green:#2fb45a;
  --ink:#2b2f3a;
  --muted:#7a8090;
  --line:#d9dde5;
  --field:#f3f5f8;
  --panel:#f7f8fa;
  --footer:#17181c;
  --stage:#eceef2;
  --white:#fff;
}
*{box-sizing:border-box;margin:0;padding:0}
html,body{width:887px;height:1200px;overflow:hidden}
body{background:var(--stage);font-family:"Open Sans",Arial,sans-serif;color:var(--ink);position:relative}
.page{position:absolute;top:24px;width:392px;background:var(--white);box-shadow:0 4px 14px rgba(0,0,0,.18);overflow:hidden}
.page--signup{left:38px;height:668px}
.page--payment{left:460px;height:1150px}

.site-header{background:var(--navy);height:26px;display:flex;align-items:center;justify-content:space-between;padding:0 14px}
.brand{display:flex;align-items:center;gap:4px;color:var(--white);font-size:7px;font-weight:700}
.brand-mark{width:8px;height:8px;background:var(--blue);border-radius:50%}
.header-contact{display:flex;gap:12px;font-size:4px;color:#c8cde0}
.header-contact b{display:block;color:var(--white);font-size:4.5px}
.main-nav{background:var(--blue);height:11px;display:flex;gap:12px;align-items:center;padding:0 14px;font-size:4px;color:var(--white);font-weight:600}

.hero{height:46px;background:linear-gradient(90deg,#1b2640,#2d3d62);display:flex;align-items:center;justify-content:center;color:var(--white);font-size:9px;font-weight:700;letter-spacing:.5px}
.hero--photo{height:62px;background:linear-gradient(90deg,#e8e2dc,#c9a892 55%,#f0ebe6)}

.notice{margin:9px 60px 0;background:var(--green);color:var(--white);font-size:4px;line-height:1.5;padding:5px 8px;text-align:center}
.intro{margin:8px 40px 0;font-size:4px;line-height:1.6;color:var(--muted);text-align:center}
.intro strong{color:var(--ink)}

.form{margin:10px 40px 0;border:1px solid var(--line);padding:10px 12px}
.form-grid{display:grid;grid-template-columns:repeat(3,1fr);gap:7px 8px}
.form-grid--two{grid-template-columns:repeat(2,1fr)}
.field label{display:block;font-size:3.8px;color:var(--muted);margin-bottom:2px}
.field span{display:block;height:9px;background:var(--field);border:1px solid var(--line)}
.btn{display:block;margin:9px auto 0;width:56px;height:12px;background:var(--blue);color:var(--white);font-size:4.5px;font-weight:700;text-align:center;line-height:12px}

.summary{margin:10px 40px 0;border:1px solid var(--line)}
.summary-row{display:grid;grid-template-columns:1fr 1fr;font-size:4px;padding:4px 10px;border-bottom:1px solid var(--line)}
.summary-row:nth-child(odd){background:var(--panel)}
.summary-row b{color:var(--ink)}
.summary-row span{color:var(--muted)}

.terms{padding:14px 40px 0}
.terms h2{text-align:center;font-size:7px;font-weight:700;color:var(--navy);margin-bottom:12px}
.terms-block{display:flex;gap:12px;margin-bottom:14px;align-items:flex-start}
.terms-block h3{font-size:5.5px;font-weight:700;color:var(--navy);margin-bottom:4px}
.terms-block p,.terms p{font-size:3.8px;line-height:1.65;color:var(--muted)}
.art{flex:0 0 70px;height:60px;border-radius:4px}
.art--billing{background:linear-gradient(135deg,#dbe7fb,#9bc0f2)}
.art--refund{background:linear-gradient(135deg,#fde9c9,#9fd3b2)}
.terms h3.plain{font-size:5.5px;font-weight:700;color:var(--navy);margin:4px 0}

.site-footer{position:absolute;left:0;right:0;bottom:0;background:var(--footer);color:#9aa0ad;padding:12px 30px 0;font-size:3.8px}
.footer-cols{display:flex;justify-content:space-between}
.footer-cols h4{color:var(--white);font-size:4.5px;margin-bottom:4px}
.footer-cols li{list-style:none;line-height:1.9}
.social{display:flex;gap:3px;margin-top:4px}
.social i{width:6px;height:6px;border-radius:50%;background:var(--blue)}
.copyright{border-top:1px solid #2b2d33;margin-top:8px;padding:4px 0;text-align:center}
</style>
</head>
<body>

<article class="page page--signup">
  <header class="site-header">
    <div class="brand"><i class="brand-mark"></i>Brightloom Rewards</div>
    <div class="header-contact"><div>Call us today<b>(800) 555-0142</b></div><div>Email us<b>hello@brightloomrewards.biz</b></div></div>
  </header>
  <nav class="main-nav"><span>Home</span><span>About</span><span>Programs</span><span>Pricing</span><span>Sign Up</span><span>Contact</span></nav>
  <div class="hero">SIGN UP</div>
  <p class="notice">Choose your program below and complete the form. Your account is ready in minutes – no contracts, cancel anytime.</p>
  <p class="intro">Reward your customers with travel and retail certificates they love. Fill in your business details, pick the plan that fits and move straight to secure payment. <strong>Questions? Our team is here 24/7 to help you get started.</strong></p>
  <div class="form">
    <div class="form-grid">
      <div class="field"><label>First Name</label><span></span></div>
      <div class="field"><label>Last Name</label><span></span></div>
      <div class="field"><label>Business Name</label><span></span></div>
      <div class="field"><label>Email</label><span></span></div>
      <div class="field"><label>Phone</label><span></span></div>
      <div class="field"><label>Website</label><span></span></div>
      <div class="field"><label>Address</label><span></span></div>
      <div class="field"><label>City</label><span></span></div>
      <div class="field"><label>Zip Code</label><span></span></div>
      <div class="field"><label>Username</label><span></span></div>
      <div class="field"><label>Password</label><span></span></div>
      <div class="field"><label>Confirm Password</label><span></span></div>
      <div class="field"><label>Program</label><span></span></div>
      <div class="field"><label>Payment Plan</label><span></span></div>
    </div>
    <span class="btn">GET STARTED</span>
  </div>
  <footer class="site-footer">
    <div class="footer-cols">
      <div><h4>Quick Links</h4><ul><li>Home</li><li>About Us</li><li>Programs</li><li>Pricing</li><li>Affiliates</li><li>Sign Up</li></ul></div>
      <div><h4>Contact Us</h4><ul><li>(800) 555-0142</li><li>hello@brightloomrewards.biz</li></ul></div>
      <div><h4>Follow Us</h4><div class="social"><i></i><i></i><i></i><i></i></div></div>
    </div>
    <div class="copyright">© Brightloom Rewards. All rights reserved.</div>
  </footer>
</article>

<article class="page page--payment">
  <header class="site-header">
    <div class="brand"><i class="brand-mark"></i>Brightloom Rewards</div>
    <div class="header-contact"><div>Call us today<b>(800) 555-0142</b></div><div>Email us<b>hello@brightloomrewards.biz</b></div></div>
  </header>
  <nav class="main-nav"><span>Home</span><span>About</span><span>Programs</span><span>Pricing</span><span>Sign Up</span><span>Contact</span></nav>
  <div class="hero hero--photo" role="img" aria-label="Photo of a smiling customer using a laptop"></div>
  <p class="intro">Almost done! Review your order and enter your card details.<br><strong>Your program starts as soon as payment is confirmed.</strong></p>
  <div class="summary">
    <div class="summary-row"><b>Program</b><span>Unlimited Program</span></div>
    <div class="summary-row"><b>Plan</b><span>$99 / month</span></div>
    <div class="summary-row"><b>Contract</b><span>None</span></div>
    <div class="summary-row"><b>Total today</b><span>$99.00</span></div>
  </div>
  <div class="form">
    <div class="form-grid form-grid--two">
      <div class="field"><label>Name on Card</label><span></span></div>
      <div class="field"><label>Card Number</label><span></span></div>
      <div class="field"><label>Expiry Date</label><span></span></div>
      <div class="field"><label>CVV</label><span></span></div>
      <div class="field"><label>Billing Address</label><span></span></div>
      <div class="field"><label>Zip Code</label><span></span></div>
    </div>
    <p class="intro" style="margin:8px 0 0;text-align:left">I agree to the payment terms and conditions below and authorize recurring billing.</p>
    <span class="btn">PAY NOW</span>
  </div>
  <section class="terms">
    <h2>PAYMENT TERMS AND CONDITIONS</h2>
    <div class="terms-block">
      <div><h3>RECURRING BILLING</h3><p>Monthly plans renew automatically on the same date each month until cancelled. Prepaid plans of six or twelve months are charged once and renew only if you choose. You may cancel at any time from your account or by contacting support; service stays active until the end of the paid period. Prices shown include all features listed for your program.</p></div>
      <div class="art art--billing" role="img" aria-label="Illustration of a calendar and credit card"></div>
    </div>
    <div class="terms-block">
      <div class="art art--refund" role="img" aria-label="Illustration of a refund receipt and coins"></div>
      <div><h3>REFUND POLICY</h3><p>Because certificates are delivered instantly, payments are not refundable once certificates have been issued. If you have not used the service, contact us within seven days of payment and we will review your request promptly.</p></div>
    </div>
    <h3 class="plain">30 DAY RISK-FREE TRIAL TERMS &amp; CONDITIONS</h3>
    <p>New members may try the program for thirty days. If you are not satisfied, cancel before the trial ends and you will not be billed. One trial per business. Certificates issued during the trial remain valid for your customers. After the trial, your chosen plan begins automatically at the listed price.</p>
  </section>
  <footer class="site-footer">
    <div class="footer-cols">
      <div><h4>Quick Links</h4><ul><li>Home</li><li>About Us</li><li>Programs</li><li>Pricing</li><li>Affiliates</li><li>Sign Up</li></ul></div>
      <div><h4>Contact Us</h4><ul><li>(800) 555-0142</li><li>hello@brightloomrewards.biz</li></ul></div>
      <div><h4>Follow Us</h4><div class="social"><i></i><i></i><i></i><i></i></div></div>
    </div>
    <div class="copyright">© Brightloom Rewards. All rights reserved.</div>
  </footer>
</article>

</body>
</html>
```